Boutique town planning business needs a Business Card design

We need a business card design for a new company called The Zoning Bridgeway. We provide town planning and urban design services to government, business and community groups. We would like to see the designs use the colours in the logo (blue, deep red, green and amber), plenty of white and including black and grey in the writing. The final design should communicate collaboration, creativity and professionalism and that we are approachable.

```html
<!DOCTYPE html>
<html lang="en">
<head>
<meta charset="utf-8">
<title>The Zoning Bridgeway – Business Card</title>
<link href="https://fonts.googleapis.com/css2?family=Exo+2:wght@400;600&display=swap" rel="stylesheet">
<style>
  :root {
    --stage: #e9e7e3;
    --card-white: #ffffff;
    --card-black: #0d0d0d;
    --band-grey: #7a7f82;
    --ink-dark: #3a3a3a;
    --ink-light: #f2f2f2;
    --brand-blue: #2f9fd0;
  }
  * { margin: 0; padding: 0; box-sizing: border-box; }
  html, body { width: 1200px; height: 901px; overflow: hidden; }
  body {
    background: var(--stage);
    font-family: "Exo 2", sans-serif;
    position: relative;
  }
  .card {
    position: absolute;
    top: 150px;
    width: 340px;
    height: 600px;
    border-radius: 38px;
    overflow: hidden;
    box-shadow: 0 14px 30px rgba(0,0,0,0.18);
  }
  .card-front { left: 230px; background: var(--card-black); }
  .card-back  { left: 630px; background: var(--card-white); }

  .front-shape { position: absolute; inset: 0; }

  .brand {
    position: absolute;
    display: flex;
    align-items: center;
    gap: 12px;
  }
  .brand-dot {
    width: 46px; height: 46px;
    border-radius: 50%;
    background: var(--brand-blue);
    flex: none;
  }
  .brand-name {
    font-weight: 600;
    font-size: 20px;
    line-height: 1.05;
    color: var(--ink-dark);
  }
  .card-front .brand { left: 36px; top: 70px; }
  .card-back .brand { left: 50%; top: 50%; transform: translate(-50%, -50%); }

  .contact {
    position: absolute;
    right: 30px;
    top: 300px;
    text-align: right;
    color: var(--ink-light);
  }
  .contact-name {
    font-weight: 600;
    font-size: 21px;
    letter-spacing: 1px;
    text-transform: uppercase;
  }
  .contact-role { font-size: 14px; margin-top: 2px; }
  .contact-address { font-size: 14px; margin-top: 18px; line-height: 1.35; }
  .contact-lines { list-style: none; margin-top: 20px; }
  .contact-lines li {
    display: flex;
    justify-content: flex-end;
    align-items: center;
    gap: 9px;
    font-size: 14px;
    line-height: 1.75;
  }
  .contact-lines svg { width: 14px; height: 14px; flex: none; }
</style>
</head>
<body>

  <section class="card card-front">
    <svg class="front-shape" viewBox="0 0 340 600" aria-hidden="true">
      <path d="M0 0 H340 V190 C300 280 150 300 0 292 Z" fill="var(--band-grey)"/>
      <path d="M0 0 H340 V168 C296 254 150 276 0 268 Z" fill="var(--card-white)"/>
    </svg>

    <div class="brand">
      <span class="brand-dot"></span>
      <span class="brand-name">The Zoning<br>Bridgeway</span>
    </div>

    <div class="contact">
      <p class="contact-name">Daniel Whitcombe</p>
      <p class="contact-role">Managing Director</p>
      <p class="contact-address">41 9th floor Arcade<br>Fieldstone Road NKV</p>
      <ul class="contact-lines">
        <li>012 555 0143
          <svg viewBox="0 0 16 16"><path d="M4 1 L6.5 4 L5 6 C6 8.5 7.5 10 10 11 L12 9.5 L15 12 L13 15 C7 14.5 1.5 9 1 3 Z" fill="var(--ink-light)"/></svg>
        </li>
        <li>012 555 0144
          <svg viewBox="0 0 16 16"><rect x="4" y="1" width="8" height="14" rx="1.5" fill="none" stroke="var(--ink-light)" stroke-width="1.6"/><circle cx="8" cy="12.5" r="0.9" fill="var(--ink-light)"/></svg>
        </li>
        <li>012 555 0145
          <svg viewBox="0 0 16 16"><rect x="2" y="6" width="12" height="8" rx="1" fill="var(--ink-light)"/><rect x="4.5" y="1.5" width="7" height="5" fill="none" stroke="var(--ink-light)" stroke-width="1.4"/></svg>
        </li>
        <li>hello@zoningbridge.com
          <svg viewBox="0 0 16 16"><rect x="1.5" y="3.5" width="13" height="9" fill="none" stroke="var(--ink-light)" stroke-width="1.4"/><path d="M1.5 3.5 L8 9 L14.5 3.5" fill="none" stroke="var(--ink-light)" stroke-width="1.4"/></svg>
        </li>
        <li>www.zoningbridgeway.com
          <svg viewBox="0 0 16 16"><circle cx="8" cy="8" r="6.5" fill="none" stroke="var(--ink-light)" stroke-width="1.3"/><ellipse cx="8" cy="8" rx="3" ry="6.5" fill="none" stroke="var(--ink-light)" stroke-width="1.1"/><path d="M1.5 8 H14.5" stroke="var(--ink-light)" stroke-width="1.1"/></svg>
        </li>
      </ul>
    </div>
  </section>

  <section class="card card-back">
    <div class="brand">
      <span class="brand-dot"></span>
      <span class="brand-name">The Zoning<br>Bridgeway</span>
    </div>
  </section>

</body>
</html>
```